KBRF website design

We need a page template website design for a cms website. Please see the brief attached for the details.
The client is the Kestrel Brook Ramfold Federation which is an organisation promoting the Ramfold Sheep Breed within Australia.
Updates

Reason: So that my top few designs can make changes and re-submit.

Target Market(s)

See attached brief

```html
<!DOCTYPE html>
<html lang="en">
<head>
<meta charset="utf-8">
<title>KBRF – Home</title>
<link href="https://fonts.googleapis.com/css2?family=Open+Sans:wght@400;600;700&family=Roboto:wght@400;500;700&family=Roboto+Condensed:wght@400;700&display=swap" rel="stylesheet">
<style>
:root{
  --green:#1e8a3a;
  --green-dark:#0f6a27;
  --cream:#f1ece2;
  --cream-soft:#faf8f4;
  --bar:#ede6d8;
  --ink:#222;
  --body:#555;
  --muted:#9a8f7c;
  --gold:#c79a4a;
  --footer:#161616;
  --footer-line:#333;
  --footer-text:#ccc;
  --yellow:#e6b800;
}
*{box-sizing:border-box;margin:0;padding:0}
html,body{width:676px;height:1200px;overflow:hidden;background:#fff}
body{position:relative;font-family:"Open Sans",sans-serif;color:var(--body)}
.abs{position:absolute}
.site-header{left:0;top:0;width:676px;height:100px;background:var(--cream)}
.brand{left:76px;top:14px;height:56px;display:flex;align-items:center;gap:8px}
.brand-mark{width:42px;height:42px;border-radius:50%;background:var(--green)}
.brand-name{font-family:"Roboto",sans-serif;font-weight:700;font-size:26px;color:var(--green)}
.header-contact{left:432px;top:21px;display:flex;gap:6px;font-family:"Roboto",sans-serif;font-size:11px;color:var(--green-dark);line-height:13px}
.header-contact b{font-size:13px;font-weight:500}
.main-nav{left:0;top:78px;width:676px;height:50px}
.nav-links{left:0;top:95px;width:676px;display:flex;justify-content:center;font-family:"Roboto",sans-serif;font-size:9.5px;font-weight:500;color:#fff;text-transform:uppercase}
.nav-links span{padding:0 11px;border-left:1px solid rgba(255,255,255,.25);line-height:14px}
.nav-links span:first-child{border-left:0}
.hero{left:0;top:110px;width:676px;height:315px;background:linear-gradient(180deg,#6fae3a 0%,#8cc63f 45%,#5f9e2a 100%)}
.hero-curve{left:0;top:395px;width:676px;height:32px}
.hero-dots{left:312px;top:414px;display:flex;gap:4px}
.hero-dots i{width:7px;height:7px;border-radius:50%;background:#ccc}
.hero-dots i:first-child{background:var(--green)}
.welcome{left:74px;top:445px;width:360px}
.welcome h1{font-family:"Roboto",sans-serif;font-size:16px;font-weight:500;color:var(--ink);margin-bottom:8px}
.welcome h1 em{font-style:normal;color:var(--green)}
.welcome p{font-size:7.4px;line-height:12px;margin-bottom:12px}
.welcome a{font-size:7.4px;color:var(--green)}
.quick-links{left:463px;top:449px;width:138px}
.quick-btn{height:30px;margin-bottom:10px;border-radius:3px;background:linear-gradient(#f3f3f3,#cfcfcf);box-shadow:0 2px 2px rgba(0,0,0,.25);display:flex;align-items:center;padding-left:10px;gap:8px;font-family:"Roboto",sans-serif;font-size:10px;color:#222}
.feed{left:0;top:582px;width:676px;height:248px;background:var(--cream-soft)}
.feed-divider{left:338px;top:582px;width:1px;height:248px;background:#ebe5da}
.feed-col h2{font-family:"Roboto Condensed",sans-serif;font-size:16px;font-weight:700;color:var(--ink);display:flex;align-items:baseline;gap:6px}
.feed-col h2 em{font-style:normal;color:var(--green)}
.feed-col h2 small{font-family:"Open Sans",sans-serif;font-style:italic;font-weight:400;font-size:6px;color:var(--muted);flex:1;border-bottom:3px solid #eee6d8;padding-bottom:1px}
.news-item{position:absolute;left:0;width:248px}
.news-thumb{position:absolute;left:0;top:0;width:40px;height:40px}
.news-date{position:absolute;left:50px;top:0;font-size:6.5px;font-style:italic;color:var(--muted)}
.news-title{position:absolute;left:50px;top:16px;font-family:"Roboto Condensed",sans-serif;font-size:9.5px;font-weight:700;color:var(--ink)}
.news-text{position:absolute;left:50px;top:33px;width:190px;font-size:7px;line-height:12px}
.rule{position:absolute;height:1px;background:#e6dfd2}
.show-all{position:absolute;height:15px;background:var(--bar);font-size:6.5px;color:#6b604e;text-align:center;line-height:15px}
.event{position:absolute;left:0;width:249px}
.event-date{position:absolute;left:0;top:0;width:42px;height:42px;background:var(--green);color:#fff;text-align:center;font-family:"Roboto Condensed",sans-serif;font-weight:700;line-height:13px;padding-top:5px}
.event-date b{font-size:16px;display:block;line-height:17px}
.event-date span{font-size:11px}
.event-title{position:absolute;left:52px;top:0;font-family:"Roboto Condensed",sans-serif;font-size:9px;font-weight:700;color:var(--ink)}
.event-text{position:absolute;left:52px;top:14px;width:190px;font-size:7px;line-height:12px}
.event-meta{position:absolute;left:70px;top:50px;display:flex;gap:14px;font-size:6px;font-style:italic;color:var(--muted);align-items:center}
.event-meta span{display:flex;gap:4px;align-items:center}
.event-meta i{width:8px;height:8px;border-radius:50%;background:var(--gold);display:inline-block}
.event-meta b{font-weight:400;color:#444}
.sponsors-title{left:0;top:847px;width:676px;text-align:center;font-family:"Roboto Condensed",sans-serif;font-size:15px;font-weight:700;color:var(--ink)}
.sponsors-title em{font-style:normal;color:var(--green)}
.sponsors-rule{left:317px;top:867px;width:22px;height:2px;background:var(--ink)}
.sponsor-row{left:74px;top:884px;display:flex;gap:14px}
.sponsor{width:94px;height:44px;border:1px solid #ddd;display:flex;align-items:center;justify-content:center}
.sponsor i{width:56px;height:14px;background:#d9d9d9;border-radius:2px}
.footer-band{left:0;top:948px;width:676px;height:3px;background:var(--yellow)}
.site-footer{left:0;top:951px;width:676px;height:249px;background:var(--footer)}
.calendar{left:74px;top:974px;width:158px;height:134px;background:#d9d9d9;border:1px solid #555;border-radius:3px;overflow:hidden}
.cal-head{height:16px;background:linear-gradient(#444,#222);color:#fff;font-size:6.5px;font-family:"Roboto",sans-serif;display:flex;justify-content:space-between;align-items:center;padding:0 5px}
.cal-head i{width:9px;height:9px;border-radius:50%;background:#555;display:block}
.cal-grid{display:grid;grid-template-columns:repeat(7,1fr);gap:1px;padding:2px;font-family:"Roboto",sans-serif;font-size:6.5px;text-align:center;color:#222}
.cal-grid span{background:#f1f1f1;height:15px;line-height:15px}
.cal-grid .dow{background:#cfcfcf;color:#555;height:12px;line-height:12px}
.cal-grid .off{color:#aaa}
.cal-grid .today{background:var(--green);color:#fff}
.footer-col{color:var(--footer-text)}
.footer-col h3{font-family:"Roboto Condensed",sans-serif;font-size:10px;font-weight:700;color:#fff;margin-bottom:12px}
.contact-line{display:flex;gap:8px;font-size:7.4px;line-height:14px;margin-bottom:10px}
.icon-dot{width:16px;height:16px;border-radius:50%;background:#3a3a3a;flex:none;display:flex;align-items:center;justify-content:center}
.social-line{display:flex;gap:8px;align-items:center;font-size:7.4px;margin-bottom:7px}
.social-line i{width:18px;height:18px;border-radius:50%;background:#fff;display:block}
.footer-nav{left:74px;top:1130px;width:528px;height:28px;border-top:1px solid var(--footer-line);border-bottom:1px solid var(--footer-line);display:flex;justify-content:space-between;align-items:center;font-size:7.4px;color:#aaa;padding:0 13px}
.copyright{left:74px;top:1174px;width:528px;display:flex;justify-content:space-between;font-size:6.8px;color:#999}
</style>
</head>
<body>

<header class="abs site-header">
  <div class="abs brand"><span class="brand-mark"></span><span class="brand-name">KBRF</span></div>
  <div class="abs header-contact">
    <svg width="14" height="20" viewBox="0 0 14 20"><path d="M3 2 L6 2 L7 6 L5 8 Q7 12 9 14 L11 12 L13 14 L13 17 Q8 18 4 12 Q1 7 3 2Z" fill="#c79a4a"/></svg>
    <div>Contact us on <b>(0400) 318-772</b><br>or email hello@kbrf-mail.org</div>
  </div>
</header>

<div class="abs hero" role="img" aria-label="Photo of a white ewe and lamb standing on green pasture in front of a wire fence"></div>

<svg class="abs main-nav" viewBox="0 0 676 50" preserveAspectRatio="none">
  <defs><linearGradient id="navg" x1="0" y1="0" x2="0" y2="1"><stop offset="0" stop-color="#2fa046"/><stop offset="1" stop-color="#0d6424"/></linearGradient></defs>
  <path d="M0 14 Q338 -6 676 14 L676 36 Q338 56 0 36Z" fill="url(#navg)"/>
</svg>
<nav class="abs nav-links">
  <span>Home</span><span>About</span><span>Search</span><span>Member Services</span><span>Stud Pages</span><span>News</span><span>Sales</span><span>Links</span><span>Contact</span>
</nav>

<svg class="abs hero-curve" viewBox="0 0 676 32" preserveAspectRatio="none"><path d="M0 32 L0 14 Q338 -14 676 14 L676 32Z" fill="#fff"/></svg>
<div class="abs hero-dots"><i></i><i></i><i></i><i></i><i></i></div>

<section class="abs welcome">
  <h1>Welcome to <em>Kestrel Brook</em></h1>
  <p>The Ramfold is an Australian breed developed for Australian conditions. The Ramfold is proving to be the ideal prime lamb terminal sire in wide-ranging areas and environments of Australia.</p>
  <p>It is giving outstanding results in the dry, arid, pastoral zones; all types of agricultural, mixed farming areas; and also in higher rainfall districts.</p>
  <a>[Read More...]</a>
</section>

<div class="abs quick-links">
  <div class="quick-btn"><svg width="14" height="14" viewBox="0 0 14 14"><circle cx="7" cy="4" r="3" fill="#222"/><path d="M1 14 Q1 8 7 8 Q13 8 13 14Z" fill="#222"/></svg>Member Resources</div>
  <div class="quick-btn"><svg width="16" height="14" viewBox="0 0 16 14"><ellipse cx="6" cy="6" rx="6" ry="4.5" fill="#222"/><ellipse cx="11" cy="9" rx="5" ry="3.5" fill="#222"/></svg>Prime Lamb Helpline</div>
  <div class="quick-btn"><svg width="12" height="14" viewBox="0 0 12 14"><path d="M3 6 V4 Q3 1 6 1 Q9 1 9 4 V6" stroke="#222" stroke-width="1.6" fill="none"/><rect x="1" y="6" width="10" height="8" rx="1" fill="#222"/></svg>WebManager Login</div>
</div>

<section class="abs feed"></section>
<div class="abs feed-divider"></div>

<div class="abs feed-col" style="left:74px;top:600px;width:248px">
  <h2>Latest <em>News</em> <small>get latest updates</small></h2>
  <div class="news-item" style="top:32px">
    <div class="news-thumb" role="img" aria-label="Photo of lamb carcasses hanging in a processing plant" style="background:linear-gradient(#c25a5a,#8e2f2f)"></div>
    <div class="news-date">15 Nov, 2014</div>
    <div class="news-title">Lamb prices forecast to rise in 2014 - 2015</div>
    <div class="news-text">Saleyard lamb prices are forecast to rise in 2014–15 on the back of tightening lamb supply and growing...</div>
  </div>
  <div class="rule" style="left:0;top:101px;width:248px"></div>
  <div class="news-item" style="top:118px">
    <div class="news-thumb" role="img" aria-label="Photo of a dark sheep standing in a paddock" style="background:linear-gradient(#a79d86,#4a4438)"></div>
    <div class="news-date">15 Nov, 2014</div>
    <div class="news-title">El Nino predicted to develop in Winter</div>
    <div class="news-text">The Weather Bureau is now predicting that it is likely (estimated at a greater than 70% chance)...</div>
  </div>
  <div class="show-all" style="left:0;top:192px;width:248px">Show All News</div>
</div>

<div class="abs feed-col" style="left:353px;top:600px;width:249px">
  <h2>Upcoming <em>Events</em> <small>get latest updates</small></h2>
  <div class="event" style="top:27px">
    <div class="event-date"><b>20</b><span>MAY</span></div>
    <div class="event-title">National Conference</div>
    <div class="event-text">2014 National Ramfold Breeders Conference was held in Hamilton, VIC Sunday 16th – Wednesday...</div>
    <div class="event-meta"><span><i></i>Live Event</span><span><i></i>Location</span><span><i></i><b>Continue Reading...</b></span></div>
  </div>
  <div class="rule" style="left:0;top:99px;width:249px"></div>
  <div class="event" style="top:111px">
    <div class="event-date"><b>20</b><span>MAY</span></div>
    <div class="event-title">POST CONFERENCE MEDIA RELEASES:</div>
    <div class="event-text">A new carcass probe with the potential to measure intra-muscular fat on-line in processing plants...</div>
    <div class="event-meta"><span><i></i>Live Event</span><span><i></i>Location</span><span><i></i><b>Continue Reading...</b></span></div>
  </div>
  <div class="show-all" style="left:0;top:192px;width:249px">Show All Events</div>
</div>

<h2 class="abs sponsors-title">Our <em>Sponsors</em></h2>
<div class="abs sponsors-rule"></div>
<div class="abs sponsor-row">
  <div class="sponsor"><i></i></div><div class="sponsor"><i></i></div><div class="sponsor"><i></i></div><div class="sponsor"><i></i></div><div class="sponsor"><i></i></div>
</div>

<div class="abs footer-band"></div>
<footer class="abs site-footer" role="img" aria-label="Dark photo of sheep grazing as footer backdrop"></footer>

<div class="abs calendar">
  <div class="cal-head"><i></i>March, 2011<i></i></div>
  <div class="cal-grid">
    <span class="dow">Sun</span><span class="dow">Mon</span><span class="dow">Tue</span><span class="dow">Wed</span><span class="dow">Thu</span><span class="dow">Fri</span><span class="dow">Sat</span>
    <span class="off">27</span><span class="off">28</span><span>1</span><span>2</span><span>3</span><span>4</span><span>5</span>
    <span>6</span><span>7</span><span>8</span><span>9</span><span>10</span><span>11</span><span>12</span>
    <span>13</span><span>14</span><span>15</span><span>16</span><span>17</span><span class="today">18</span><span>19</span>
    <span>20</span><span>21</span><span>22</span><span>23</span><span>24</span><span>25</span><span>26</span>
    <span>27</span><span>28</span><span>29</span><span>30</span><span>31</span><span class="off">1</span><span class="off">2</span>
    <span class="off">3</span><span class="off">4</span><span class="off">5</span><span class="off">6</span><span class="off">7</span><span class="off">8</span><span class="off">9</span>
  </div>
</div>

<div class="abs footer-col" style="left:310px;top:970px;width:160px">
  <h3>Get in Touch</h3>
  <div class="contact-line"><span class="icon-dot"><svg width="8" height="10" viewBox="0 0 8 10"><path d="M4 0 Q8 0 8 4 Q8 6 4 10 Q0 6 0 4 Q0 0 4 0Z" fill="#ccc"/></svg></span>PO Box 417, Eastfield,<br>SA 5099</div>
  <div class="contact-line"><span class="icon-dot"><svg width="9" height="8" viewBox="0 0 9 8"><rect x="0" y="2" width="9" height="6" rx="1" fill="#ccc"/><rect x="2" y="0" width="5" height="3" fill="#ccc"/></svg></span>(08) 8300-1142</div>
  <div class="contact-line"><span class="icon-dot"><svg width="9" height="9" viewBox="0 0 9 9"><rect x="0" y="3" width="9" height="4" fill="#ccc"/><rect x="2" y="0" width="5" height="9" fill="none" stroke="#ccc"/></svg></span>(08) 8300-1187</div>
  <div class="contact-line"><span class="icon-dot"><svg width="9" height="7" viewBox="0 0 9 7"><rect width="9" height="7" fill="#ccc"/><path d="M0 0 L4.5 4 L9 0" stroke="#3a3a3a" fill="none"/></svg></span>hello@kbrf-mail.org</div>
</div>

<div class="abs footer-col" style="left:491px;top:970px;width:110px">
  <h3>Let's be Social</h3>
  <div class="social-line"><i></i>Friendbook</div>
  <div class="social-line"><i></i>Chirper</div>
  <div class="social-line"><i></i>Circles</div>
</div>

<nav class="abs footer-nav">
  <span>Home</span><span>About</span><span>Search</span><span>Member Services</span><span>Stud Pages</span><span>News</span><span>Sales</span><span>Links</span><span>Contact</span>
</nav>
<div class="abs copyright">
  <span>Copyright © 2014 Kestrel Brook Ramfold Federation. All Rights Reserved.</span>
  <span>Website design and development by Larkline Studio</span>
</div>

</body>
</html>
```